inspirational business card

I want to use the Vector on Pixavend.com (number 58172046) and I will purchase the vector to send it to the designer once the general concept is approved. You can download it for free for a one time use on providing a design for this request.
Within the vector, insert:
Tessa Brundle
Guidance and Partnering

I prefer a vertical card but do not require vertical.

Contact info:

Tessa Brundle, J.D.
Collaborative Lawyer
Certified Divorce Coach
Mediation Coach
PHONE 515/555-0143
EMAIL: tbjd@quellmail.net

Website: Guidanceandpartnering.com
Settlementcourse.com

I like greens, blue and grey. I do not want black font, and would like the font to be legible without needing perfect reading vision (no super small font).
I would like the overall theme to convey growth and nurturance.
I like the vector I selected because of the growth and light portrayed.
Not too frilly or too bold. I would like to to appeal to both sexes.

Target Market(s)

Generally professional women 35-60

Industry/Entity Type

Attorney

Font styles to use
Serif
Sans Serif

Colors
acd136
cadf82
fbf289
9d9d9d

Requirements
Must have
• My project does not need to have my photo but you could use it if you want
Nice to have
• Vertical
• I like rounded edges on the cards
Should not have
• I do not like my name appearing two times in close proximity. I'm not a flowery person.

```html
<!DOCTYPE html>
<html lang="en">
<head>
<meta charset="utf-8">
<title>Tessa Brundle – Business Card</title>
<link href="https://fonts.googleapis.com/css2?family=Tinos&family=Source+Sans+3:wght@400&display=swap" rel="stylesheet">
<style>
  :root {
    --stage: #444444;
    --cream: #fdf48c;
    --cream-edge: #cadf82;
    --leaf: #7a9c40;
    --leaf-soft: #d6e68f;
    --slate: #7a7b8c;
    --ink-light: #f8ef88;
  }
  * { margin: 0; padding: 0; box-sizing: border-box; }
  html, body { width: 1200px; height: 1200px; overflow: hidden; background: var(--stage); }
  .stage { position: relative; width: 1200px; height: 1200px; }

  .card-front {
    position: absolute; left: 22px; top: 18px; width: 570px; height: 996px;
    background: var(--cream); border: 9px solid var(--cream-edge); overflow: hidden;
  }
  .brand-emblem { position: absolute; left: 140px; top: 227px; width: 276px; height: 276px; }
  .brand-name {
    position: absolute; left: 0; width: 552px; top: 540px; text-align: center;
    font-family: "Tinos", "Times New Roman", serif; color: var(--slate);
    font-size: 50px; line-height: 1; letter-spacing: 0.5px;
  }
  .brand-tagline {
    position: absolute; left: 0; width: 552px; top: 593px; text-align: center;
    font-family: "Tinos", "Times New Roman", serif; color: var(--slate);
    font-size: 22px; line-height: 1; letter-spacing: 0.3px;
  }
  .foliage-accent { position: absolute; left: 120px; top: 655px; width: 432px; height: 332px; }

  .card-back {
    position: absolute; left: 614px; top: 183px; width: 570px; height: 995px;
    background: var(--cream); overflow: hidden;
  }
  .back-shapes { position: absolute; inset: 0; }
  .portrait { position: absolute; left: 26px; top: 291px; width: 216px; height: 216px; }
  .contact {
    position: absolute; left: 25px; top: 524px;
    font-family: "Source Sans 3", "Myriad Pro", sans-serif; color: var(--ink-light);
  }
  .contact-name { font-size: 40px; line-height: 48px; }
  .contact-roles { font-size: 26px; line-height: 36px; margin-top: 2px; }
  .contact-details { font-size: 29px; line-height: 35px; margin-top: 32px; }
</style>
</head>
<body>
<div class="stage">

  <section class="card-front">
    <svg class="brand-emblem" viewBox="0 0 276 276" role="img" aria-label="Tree of life emblem in green within a crescent circle">
      <circle cx="138" cy="138" r="138" fill="#9ab85a"/>
    </svg>
    <div class="brand-name">TESSA BRUNDLE</div>
    <div class="brand-tagline">GUIDANCE AND PARTNERING</div>
    <svg class="foliage-accent" viewBox="0 0 432 332" role="img" aria-label="Faint leafy tree branches decoration">
      <defs>
        <radialGradient id="foliageGlow" cx="1" cy="1" r="1">
          <stop offset="0" stop-color="#d6e68f"/>
          <stop offset="0.75" stop-color="#e6ec8d"/>
          <stop offset="1" stop-color="#fdf48c"/>
        </radialGradient>
      </defs>
      <path d="M0,332 Q20,40 432,0 V332 Z" fill="url(#foliageGlow)"/>
    </svg>
  </section>

  <section class="card-back">
    <svg class="back-shapes" viewBox="0 0 570 995">
      <path d="M0,2 Q340,-8 570,300 V995 H0 Z" fill="var(--cream-edge)"/>
      <path d="M0,35 Q330,25 534,270 V995 H0 Z" fill="var(--leaf)"/>
      <rect x="543" y="282" width="9" height="713" fill="var(--leaf)"/>
      <rect x="559" y="300" width="11" height="695" fill="var(--cream-edge)"/>
      <circle cx="134" cy="399" r="108" fill="var(--ink-light)"/>
    </svg>
    <svg class="portrait" viewBox="0 0 216 216" role="img" aria-label="Portrait photo of Tessa Brundle">
      <defs>
        <radialGradient id="portraitTone" cx="0.5" cy="0.4" r="0.6">
          <stop offset="0" stop-color="#6a6f78"/>
          <stop offset="1" stop-color="#2a2d33"/>
        </radialGradient>
      </defs>
      <circle cx="108" cy="108" r="101" fill="url(#portraitTone)"/>
    </svg>
    <div class="contact">
      <div class="contact-name">Tessa Brundle, J.D.</div>
      <div class="contact-roles">
        Collaborative Lawyer<br>
        Certified Divorce Coach<br>
        Mediation Coach
      </div>
      <div class="contact-details">
        515/555-0143<br>
        tbjd@quellmail.net<br>
        guidanceandpartnering.com<br>
        settlementcourse.com
      </div>
    </div>
  </section>

</div>
</body>
</html>
```